Bright Arch Group business card

Bright Arch Group is the parent company of Bright Arch Building, Bright Arch Plumbing and Bright Arch Renovating. We require a sophisticated business card that covers all aspects of the building and plumbing space without using told or construction items.

Industry/Entity Type

Construction Company

Contact Information for Business Card

Gareth Pimley
Director
0472915083
gareth@brightarch.com.au
Www.brightarch.com.au

Font styles to use
Serif
Sans Serif

Colors
3176b5
ffce3e
0692cd
34a7d8
fbee3e
faa54b

Requirements
Must have
• Logo on front
• Logo and details on rear.
Nice to have
• Maybe water mark or shadow effect with logo
Should not have
• Tools or any construction associated items

```html
<!DOCTYPE html>
<html lang="en">
<head>
<meta charset="utf-8">
<title>Bright Arch Group – Business Card</title>
<link rel="stylesheet" href="https://fonts.googleapis.com/css2?family=Jost:wght@400&family=Oswald:wght@500&family=Lato:wght@400&display=swap">
<style>
  :root {
    --backdrop: #4b3122;
    --card-white: #ffffff;
    --card-black: #030303;
    --accent: #f58220;
    --ink: #111111;
    --muted: #555555;
    --rule: #9a9a9a;
  }
  * { margin: 0; padding: 0; box-sizing: border-box; }
  html, body { width: 1200px; height: 960px; overflow: hidden; }
  body { background: var(--backdrop); position: relative; }

  .card {
    position: absolute;
    left: 257px;
    width: 703px;
    height: 401px;
    box-shadow: 0 4px 10px rgba(0,0,0,0.35);
  }
  .card--front { top: 52px; background: var(--card-white); }
  .card--back  { top: 508px; background: var(--card-black); }

  .brand {
    position: absolute;
    left: 0; right: 0;
    text-align: center;
  }
  .brand__dot {
    display: block;
    margin: 0 auto;
    width: 34px; height: 34px;
    border-radius: 50%;
    background: var(--accent);
  }
  .brand__name {
    display: block;
    margin-top: 22px;
    font-family: "Jost", sans-serif;
    font-weight: 400;
    font-size: 32px;
    letter-spacing: 7px;
    padding-left: 7px;
  }
  .card--front .brand { top: 92px; }
  .card--front .brand__name { color: var(--ink); }
  .card--back .brand { top: 140px; }
  .card--back .brand__name { color: #ffffff; font-size: 36px; letter-spacing: 8px; }

  .person {
    position: absolute;
    right: 375px;
    top: 262px;
    text-align: right;
  }
  .person__name {
    font-family: "Oswald", sans-serif;
    font-weight: 500;
    font-size: 27px;
    line-height: 1.1;
    color: var(--accent);
    text-transform: uppercase;
    letter-spacing: -0.3px;
  }
  .person__role {
    font-family: "Lato", sans-serif;
    font-size: 18px;
    color: var(--muted);
    margin-top: 2px;
  }

  .divider {
    position: absolute;
    left: 351px;
    top: 260px;
    width: 1px;
    height: 64px;
    background: var(--rule);
  }

  .contacts {
    position: absolute;
    left: 397px;
    top: 257px;
    list-style: none;
  }
  .contacts li {
    display: flex;
    align-items: center;
    height: 22px;
    margin-bottom: 1px;
    font-family: "Lato", sans-serif;
    font-size: 16px;
    color: var(--muted);
  }
  .contacts .icon {
    width: 17px; height: 17px;
    margin-right: 12px;
    border-radius: 4px;
    background: var(--accent);
    flex: none;
  }

  .web {
    position: absolute;
    left: 0; right: 0;
    top: 327px;
    text-align: center;
    font-family: "Lato", sans-serif;
    font-size: 16px;
    letter-spacing: 3px;
    color: #ffffff;
  }
</style>
</head>
<body>

<section class="card card--front">
  <div class="brand">
    <span class="brand__dot"></span>
    <span class="brand__name">BRIGHT ARCH GROUP</span>
  </div>

  <div class="person">
    <p class="person__name">Gareth Pimley</p>
    <p class="person__role">Director</p>
  </div>

  <div class="divider"></div>

  <ul class="contacts">
    <li>
      <svg class="icon" viewBox="0 0 17 17" aria-hidden="true">
        <path d="M6 4.5c.6 0 1 1.6 1 2.2 0 .5-.8.7-.8 1.2 0 .8 1.5 2.3 2.3 2.3.5 0 .7-.8 1.2-.8.6 0 2.2.4 2.2 1 0 .9-1 1.6-1.9 1.6C7 12 5 10 5 6.4 5 5.5 5.4 4.5 6 4.5z" fill="#fff"/>
      </svg>
      0472915083
    </li>
    <li>
      <svg class="icon" viewBox="0 0 17 17" aria-hidden="true">
        <rect x="4" y="5.5" width="9" height="6.5" fill="none" stroke="#fff" stroke-width="1.1"/>
        <path d="M4 5.8l4.5 3.6L13 5.8" fill="none" stroke="#fff" stroke-width="1.1"/>
      </svg>
      gareth@brightarch.com.au
    </li>
    <li>
      <svg class="icon" viewBox="0 0 17 17" aria-hidden="true">
        <circle cx="8.5" cy="8.5" r="4.5" fill="none" stroke="#fff" stroke-width="1.1"/>
        <ellipse cx="8.5" cy="8.5" rx="2" ry="4.5" fill="none" stroke="#fff" stroke-width="1"/>
        <path d="M4 8.5h9" stroke="#fff" stroke-width="1"/>
      </svg>
      www.brightarch.com.au
    </li>
  </ul>
</section>

<section class="card card--back">
  <div class="brand">
    <span class="brand__dot"></span>
    <span class="brand__name">BRIGHT ARCH GROUP</span>
  </div>
  <p class="web">www.brightarch.com.au</p>
</section>

</body>
</html>
```